依頼詳細
販売店舗数45店にて店で配るチラシにも使用。
基本的に店舗にてド注文を頂きますので、フライヤーの下記に注文書などが付いていると
とても便利です。(お客様控え・店舗控え)

大きさはB4サイズ、商品は2品のみです。
商品:おせち料理3段重 13,950円  おせち料理与段重19,500円

三段重と与段(ヨダン)重は縁起を担いでのネーミングです。
詳しくは当社ホームページにて
http://www.kuremadeli.co.jp

記載項目
株式会社クレマデリカ(茨城県 水戸市)
おせち料理監修 株式会社波音鮨東雲グループ(広島県 福山市)

おせち料理三段重 13,950円
おせち料理与段重 19,500円

鮮度とおいしさを追及すると生おせちです。
大きなロブスターとタラバガニを溢れんばかりに詰め込みました。
寿し屋が取り扱う海産物同様、「鮮度は味」をおせち料理で形にしました。

全国配送無料
配送不可能エリア:北海道・沖縄・離島
生おせちなので製造が12月30日にすべての商品を製造します。製造できた商品から冷蔵車
にて発送されるため、関東から北海道内は12月31日に到着しない恐れがあります(天候・道路状況)
そのため、北海道はエリア外とさせて頂きます。

西日本は広島県福山市にて製造・配送を行います。沖縄・離島は上記同様です。

サイズ
B4
ページ数
片面
希望イメージ
シンプル 複雑
単色 カラフル
暗い 明るい
日常 高級
遊び心 厳粛
未来的 伝統的
女性的 男性的
希望する色
全体的に雅な色使い
納品ファイル
• 高解像度JPG (.jpg)
• イラストレーター形式 (.ai)
• フォトショップ形式 (.psd)
補足説明
制作にあたり当社にて今年の商材を撮影をしましたデータを追記致します。
まだ、何ショットかありますが、とりあえず4点追記します。

商品は3段のものと、タラバガニが入った4段(1~3段は同等品)
の2種類です。

宜しくお願いします。
当社おせち料理の成分表を掲載します。
参考までにご利用ください。
おせち料理3段データを追記します。

大変失礼しました。
素材が少ないかもしれませんので、追記します。
ご使用いただければ幸いです。
ご提案の点数が少なく絞り込む材料がないので期間を延長させて頂きます。
いよいよおせち商戦が始まりました。
すでにオーダーが入ってきたために、至急店舗に掲示を致します。
数多くのご参加が頂ければ幸いです。
納得いく作品がまだ出ていないので延長をさせて頂きます。
宜しくお願いします。

商品の写真がさほどいいものではなかったにも関わらず、最大限に魅力を出していただけました。
お客様が商品を選ぶ時に「見易さ・選択肢しやすい」がきちんと作品に出していただけました。

商品の写真が少なかったにも関わらず、たくさんのご参加を頂きましてありがとうございました。会社として大きな商談になる年末の商品は私たちにとってとても大切なものです。
会社社員と店舗の従業員で売りやすさと訴求力を重視して決めさせていただきました。
参加を頂いた皆様に社員一同より御礼申し上げます。

```html
<!DOCTYPE html>
<html lang="ja">
<head>
<meta charset="utf-8">
<title>生おせち料理 2013年新春 ご予約チラシ</title>
<link href="https://fonts.googleapis.com/css2?family=Noto+Serif+JP:wght@500;700;900&family=Noto+Sans+JP:wght@400;700;900&family=Yuji+Syuku&display=swap" rel="stylesheet">
<style>
:root{
  --purple-deep:#3d1450;
  --purple:#6a2c82;
  --purple-light:#9a5fb2;
  --lilac:#d8c3e3;
  --gold:#e8c766;
  --gold-pale:#f6e7b0;
  --red:#c8102e;
  --white:#ffffff;
  --ink:#2a1a30;
  --paper:#fbf7fc;
}
*{margin:0;padding:0;box-sizing:border-box}
html,body{width:855px;height:1200px;overflow:hidden;background:var(--white)}
.flyer{position:relative;width:855px;height:1200px;overflow:hidden;
  background:linear-gradient(160deg,#7b3a94 0%,var(--purple) 45%,var(--purple-deep) 100%);
  font-family:"Noto Sans JP",sans-serif;color:var(--white)}
.pattern{position:absolute;inset:0 0 290px 0;
  background:radial-gradient(circle at 80% 20%,rgba(255,255,255,.14),transparent 55%),
             radial-gradient(circle at 20% 70%,rgba(255,255,255,.08),transparent 50%)}
.tagline{position:absolute;left:30px;top:22px;padding:6px 22px;
  background:var(--purple-deep);border:2px solid var(--gold);
  font-family:"Noto Serif JP",serif;font-weight:900;font-size:24px;color:var(--gold-pale);letter-spacing:.08em}
.photo{position:absolute;border:3px solid var(--white);box-shadow:0 3px 8px rgba(0,0,0,.4)}
.photo-three{left:22px;top:66px;width:400px;height:228px;
  background:linear-gradient(135deg,#2b1a1a,#8c3a2a 40%,#d9a24a 70%,#3a2020)}
.price-three{position:absolute;left:30px;top:300px;color:var(--white)}
.price-three .caption{font-size:13px;color:var(--gold-pale)}
.price-three .amount{font-family:"Noto Serif JP",serif;font-weight:900;font-size:40px;line-height:1;color:var(--white)}
.price-three .amount small{font-size:20px}
.free-ship{position:absolute;width:56px;height:56px;border-radius:50%;background:var(--red);
  color:var(--white);font-size:12px;font-weight:700;display:flex;align-items:center;justify-content:center;text-align:center;line-height:1.2}
.free-a{left:330px;top:298px}
.season{position:absolute;right:58px;top:24px;writing-mode:vertical-rl;
  font-family:"Noto Serif JP",serif;font-weight:700;font-size:20px;color:var(--gold-pale);letter-spacing:.1em}
.early{position:absolute;right:96px;top:30px;width:100px;background:var(--red);border:2px solid var(--gold);
  text-align:center;padding:6px 0;font-weight:900;font-size:19px;line-height:1.1}
.early span{display:block;font-size:11px;font-weight:400}
.reserve-note{position:absolute;left:446px;top:60px;writing-mode:vertical-rl;font-size:15px;font-weight:700;color:var(--gold-pale)}
.title-raw{position:absolute;left:480px;top:40px;font-family:"Yuji Syuku",serif;font-size:190px;line-height:1;
  color:var(--gold);text-shadow:2px 3px 0 var(--purple-deep)}
.title-osechi{position:absolute;left:605px;top:232px;writing-mode:vertical-rl;font-family:"Yuji Syuku",serif;
  font-size:58px;line-height:1;color:var(--white)}
.title-ryouri{position:absolute;left:500px;top:232px;writing-mode:vertical-rl;font-family:"Yuji Syuku",serif;
  font-size:46px;line-height:1;color:var(--white)}
.lead{position:absolute;left:680px;top:200px;height:240px;width:130px;writing-mode:vertical-rl;
  font-family:"Noto Serif JP",serif;font-size:12px;line-height:1.7;color:var(--white)}
.lead em{font-style:normal;color:var(--gold)}
.tier-grid{position:absolute;left:22px;top:352px;width:811px;height:560px}
.tier{position:absolute;border:3px solid var(--white);box-shadow:0 3px 8px rgba(0,0,0,.4)}
.tier-1{left:300px;top:0;width:260px;height:200px;background:linear-gradient(135deg,#3a2418,#c0603a 50%,#e8c070)}
.tier-2{left:0;top:30px;width:290px;height:290px;background:linear-gradient(140deg,#5a1a10,#d04a2a 45%,#f09050 80%,#3a1a10)}
.tier-3{left:440px;top:210px;width:371px;height:220px;background:linear-gradient(135deg,#2a1a12,#9a6a3a 45%,#d8b06a 75%,#4a2a1a)}
.tier-4{left:0;top:330px;width:430px;height:230px;background:linear-gradient(150deg,#6a1a12,#d05a3a 40%,#f2a070 70%,#7a2a1a)}
.tier-label{position:absolute;writing-mode:vertical-rl;background:var(--red);color:var(--white);
  font-family:"Noto Serif JP",serif;font-weight:900;font-size:20px;padding:8px 4px;border:2px solid var(--gold)}
.label-1{left:260px;top:6px}
.label-2{left:258px;top:210px}
.label-3{left:570px;top:220px}
.label-4{left:30px;top:420px}
.price-four{position:absolute;left:470px;top:790px;display:flex;align-items:center;gap:10px}
.crab-badge{width:130px;padding:6px;background:var(--gold);color:var(--purple-deep);text-align:center;
  font-weight:900;font-size:18px;line-height:1.2}
.crab-badge span{display:block;font-size:11px;font-weight:700}
.price-four .amount{font-family:"Noto Serif JP",serif;font-weight:900;font-size:54px;color:var(--white);line-height:1}
.price-four .amount small{font-size:26px}
.free-b{left:780px;top:730px}
.phone-band{position:absolute;left:0;top:918px;width:855px;height:44px;background:var(--white);color:var(--purple-deep);
  display:flex;align-items:center;padding:0 28px;gap:14px;font-weight:700;font-size:14px}
.phone-band .number{display:flex;align-items:center;gap:6px;font-size:32px;font-weight:900;color:var(--purple)}
.phone-band .hours{margin-left:auto;font-size:12px;text-align:right;line-height:1.3}
.company{position:absolute;left:0;top:962px;width:855px;height:38px;background:var(--purple-deep);
  display:flex;align-items:center;padding:0 28px;gap:20px;font-size:11.5px;color:var(--lilac)}
.company strong{color:var(--white);font-size:13px}
.order-area{position:absolute;left:0;top:1000px;width:855px;height:200px;background:var(--paper);
  display:flex;gap:20px;padding:12px 22px;color:var(--ink)}
.order-form{flex:1;border:1.5px solid var(--purple);font-size:11px}
.order-form h2{background:var(--purple);color:var(--white);font-size:13px;padding:4px 8px;font-weight:700}
.order-form table{width:100%;border-collapse:collapse}
.order-form td{border:1px solid var(--lilac);padding:5px 6px;height:26px}
.order-form td.key{width:30%;background:#f1e8f5;color:var(--purple-deep);font-weight:700}
</style>
</head>
<body>
<main class="flyer">
  <div class="pattern" role="img" aria-label="雅な紫地に金の和柄模様"></div>

  <div class="tagline">厳選素材で鮮度抜群</div>
  <div class="photo photo-three" role="img" aria-label="おせち料理三段重の写真"></div>
  <div class="price-three">
    <div class="caption">おせち料理三段重（税込）</div>
    <div class="amount">13,950<small>円</small></div>
  </div>
  <div class="free-ship free-a">送料<br>無料</div>

  <div class="early"><span>11月30日まで</span>早期割引中</div>
  <div class="season">２０１３年新春</div>
  <div class="reserve-note">ご予約承り中</div>
  <div class="title-raw">生</div>
  <div class="title-osechi">おせち</div>
  <div class="title-ryouri">料理</div>
  <p class="lead">鮮度とおいしさを追求すると生おせちです。大きなロブスターとタラバガニを溢れんばかりに詰め込みました。寿し屋が取り扱う海産物同様、<em>「鮮度は味」</em>をおせち料理で形にしました。</p>

  <section class="tier-grid">
    <div class="tier tier-1" role="img" aria-label="一の重の料理写真"></div>
    <div class="tier tier-2" role="img" aria-label="二の重のロブスター入り料理写真"></div>
    <div class="tier tier-3" role="img" aria-label="三の重の料理写真"></div>
    <div class="tier tier-4" role="img" aria-label="与の重のタラバガニ写真"></div>
    <div class="tier-label label-1">一の重</div>
    <div class="tier-label label-2">二の重</div>
    <div class="tier-label label-3">三の重</div>
    <div class="tier-label label-4">与の重</div>
  </section>

  <div class="free-ship free-b">送料<br>無料</div>
  <div class="price-four">
    <div class="crab-badge">たらば3本入<span>おせち料理与段重</span></div>
    <div class="amount">19,500<small>円</small></div>
  </div>

  <div class="phone-band">
    <span>お電話でおせちご予約のお客様は</span>
    <span class="number">
      <svg width="30" height="30" viewBox="0 0 24 24" aria-hidden="true"><path fill="#6a2c82" d="M6.6 10.8a15.1 15.1 0 0 0 6.6 6.6l2.2-2.2a1 1 0 0 1 1-.25 11.4 11.4 0 0 0 3.6.57 1 1 0 0 1 1 1V20a1 1 0 0 1-1 1A17 17 0 0 1 3 4a1 1 0 0 1 1-1h3.5a1 1 0 0 1 1 1c0 1.25.2 2.45.57 3.57a1 1 0 0 1-.25 1z"/></svg>
      029-555-0184
    </span>
    <span class="hours">受付時間 9:00〜17:00<br>配送不可：北海道・沖縄・離島</span>
  </div>

  <div class="company">
    <strong>株式会社クレマデリカ</strong>
    <span>茨城県水戸市青葉台1-2-3</span>
    <span>http://www.kuremadeli.co.jp</span>
    <span>おせち料理監修 株式会社波音鮨東雲グループ</span>
  </div>

  <section class="order-area">
    <div class="order-form">
      <h2>おせちご予約申込書（お客様控え）</h2>
      <table>
        <tr><td class="key">三段重 13,950円</td><td>個数　　　個</td></tr>
        <tr><td class="key">与段重 19,500円</td><td>個数　　　個</td></tr>
        <tr><td class="key">お名前</td><td></td></tr>
        <tr><td class="key">お電話番号</td><td></td></tr>
        <tr><td class="key">お受取日</td><td>12月31日</td></tr>
      </table>
    </div>
    <div class="order-form">
      <h2>おせちご予約申込書（店舗控え）</h2>
      <table>
        <tr><td class="key">三段重 13,950円</td><td>個数　　　個</td></tr>
        <tr><td class="key">与段重 19,500円</td><td>個数　　　個</td></tr>
        <tr><td class="key">お名前</td><td></td></tr>
        <tr><td class="key">お電話番号</td><td></td></tr>
        <tr><td class="key">受付店舗</td><td></td></tr>
      </table>
    </div>
  </section>
</main>
</body>
</html>
```